Do it yourself Karten und Hochzeitsdeko selbstgemacht
Zielgruppe
Wir sind ein Bastelgeschäft. Wir bieten Materialien zum selber machen von Karten, Tischkarten,Menükarten, Gästebüchern, Fotoalben an.
Alle Materialien zur Anlassgestaltung, auch Tischdeko und Kerzen.
Zielgruppe: Junge Leute auf einer Hochzeitsmesse
Aufgabenstellung
Ich benötige einen Flyer in A5 Format. Einige Fotoausschnitte und Text. Romantisch.
Fotos von angefertigten Karten und Deko sind vorhanden.
Logo vorhanden, soll mit rein und Öffnungszeiten mit Internet
Text: Do it Yourself Karten und Hochzeitsdeko selbst gemacht!
Zeiten etc. bitte www.falten-und-kleben.example

```html
<!DOCTYPE html>
<html lang="de">
<head>
<meta charset="utf-8">
<title>Behrens – Do it yourself Flyer</title>
<link rel="stylesheet" href="https://fonts.googleapis.com/css2?family=Pinyon+Script&family=Crimson+Text:wght@400&display=swap">
<style>
  :root {
    --teal: #4b97a2;
    --teal-dark: #3e8690;
    --pattern-light: #ecebea;
    --pattern-mid: #dedbd9;
    --pattern-deep: #d3d0ce;
    --panel-light: #f6f5f4;
    --panel-mid: #ebe9e7;
    --ink: #6e6c6a;
    --white: #ffffff;
    --stage: #ffffff;
  }
  * { box-sizing: border-box; margin: 0; padding: 0; }
  html, body { width: 1200px; height: 900px; overflow: hidden; background: var(--stage); }
  body { position: relative; font-family: "Crimson Text", Georgia, serif; }

  .flyer {
    position: absolute; top: 68px; width: 540px; height: 764px;
    overflow: hidden; box-shadow: 0 6px 18px rgba(0,0,0,.18);
  }
  .flyer--front { left: 40px; }
  .flyer--back { left: 620px; }

  .damask {
    position: absolute; inset: 0;
    background:
      radial-gradient(ellipse 60% 30% at 25% 8%, var(--pattern-light), transparent 70%),
      radial-gradient(ellipse 60% 30% at 80% 95%, var(--pattern-light), transparent 70%),
      radial-gradient(ellipse 80% 50% at 50% 50%, var(--pattern-mid), var(--pattern-deep));
  }

  .band { position: absolute; left: 0; right: 0; background: var(--teal); z-index: 2; }
  .band::before, .band::after {
    content: ""; position: absolute; left: 6px; right: 6px;
    border-top: 2px dotted rgba(255,255,255,.85);
  }
  .band::before { top: 5px; }
  .band::after { bottom: 5px; }

  .photo { position: absolute; z-index: 1; }

  .badge {
    position: absolute; width: 132px; height: 132px; border-radius: 50%;
    background: var(--teal-dark); border: 3px solid var(--white);
    box-shadow: 0 0 0 3px var(--teal-dark);
    display: flex; align-items: center; justify-content: center;
    color: var(--white); font-size: 28px; letter-spacing: .5px; z-index: 4;
  }

  /* Front */
  .flyer--front .band--top { top: 100px; height: 66px; }
  .flyer--front .photo {
    top: 166px; left: 10px; right: 10px; height: 430px;
    background:
      radial-gradient(ellipse 35% 45% at 15% 40%, rgba(176,160,120,.75), transparent 70%),
      radial-gradient(ellipse 45% 30% at 30% 92%, rgba(70,95,70,.55), transparent 70%),
      radial-gradient(ellipse 30% 25% at 85% 85%, rgba(120,130,100,.5), transparent 70%),
      radial-gradient(ellipse 50% 45% at 60% 45%, #f5f5f7, transparent 75%),
      linear-gradient(135deg, #a9a08a 0%, #d9d8d5 35%, #ececee 60%, #bfc0c2 100%);
  }
  .flyer--front .badge { left: 204px; top: 66px; }
  .flyer--front .band--bottom { top: 596px; height: 112px; }
  .headline {
    position: absolute; left: 70px; top: 604px; color: var(--white); z-index: 3;
    font-family: "Pinyon Script", cursive; font-weight: 400; font-size: 44px; line-height: 1.2;
  }
  .subline {
    position: absolute; left: 150px; top: 666px; color: var(--white); z-index: 3;
    font-size: 20px; letter-spacing: .3px;
  }

  /* Back */
  .flyer--back .band--top { top: 58px; height: 64px; }
  .flyer--back .badge { left: 300px; top: 24px; }
  .flyer--back .photo {
    top: 122px; left: 0; width: 150px; height: 470px;
    background:
      radial-gradient(ellipse 40% 12% at 45% 28%, rgba(50,90,55,.6), transparent 70%),
      radial-gradient(ellipse 45% 20% at 50% 75%, #f3f3f5, transparent 75%),
      linear-gradient(180deg, #d0d0d6 0%, #efeff1 25%, #c4c8c0 50%, #e6e6e9 75%, #bfc0c4 100%);
  }
  .info-panel {
    position: absolute; top: 122px; left: 150px; right: 0; height: 470px;
    padding: 58px 40px 0 50px; color: var(--ink); z-index: 1;
  }
  .info-panel::before {
    content: ""; position: absolute; inset: 0; z-index: -1;
    background:
      radial-gradient(ellipse 50% 35% at 70% 30%, var(--panel-mid), transparent 70%),
      radial-gradient(ellipse 50% 35% at 30% 80%, var(--panel-mid), transparent 70%),
      var(--panel-light);
  }
  .info-title {
    font-family: "Pinyon Script", cursive; color: var(--teal);
    font-size: 30px; font-weight: 400; margin-bottom: 12px;
  }
  .hours { display: grid; grid-template-columns: 1fr auto; row-gap: 2px; font-size: 16px; margin-bottom: 44px; }
  .hours dd { text-align: right; }
  .contact { font-size: 16px; line-height: 1.5; font-style: normal; }
  .contact-lines { list-style: none; margin-top: 16px; }
  .contact-lines li { display: flex; align-items: center; gap: 10px; }
  .contact-lines svg { width: 14px; height: 14px; fill: var(--teal); flex: none; }
  .flyer--back .band--bottom { top: 592px; height: 116px; }
  .claim {
    position: absolute; left: 40px; top: 606px; color: var(--white); z-index: 3;
    font-size: 21px; letter-spacing: .3px;
  }
  .slogan {
    position: absolute; right: 30px; top: 636px; color: var(--white); z-index: 3;
    font-family: "Pinyon Script", cursive; font-weight: 400; font-size: 48px;
  }
</style>
</head>
<body>

<section class="flyer flyer--front">
  <div class="damask" role="img" aria-label="Hellgraues Damastmuster als Hintergrund"></div>
  <div class="band band--top"></div>
  <div class="photo" role="img" aria-label="Foto selbst gestalteter Hochzeitskarten, Menükarte, Serviette mit Herz, Windlichter mit Buchsbaumherzen und Dankeskarte"></div>
  <div class="badge">Behrens</div>
  <div class="band band--bottom"></div>
  <h1 class="headline">Do it yourself</h1>
  <p class="subline">Karten &amp; Hochzeitsdeko selbst gemacht</p>
</section>

<section class="flyer flyer--back">
  <div class="damask" role="img" aria-label="Hellgraues Damastmuster als Hintergrund"></div>
  <div class="band band--top"></div>
  <div class="badge">Behrens</div>
  <div class="photo" role="img" aria-label="Fotostreifen mit gefalteten Karten und Buchsbaumherz-Dekoration"></div>
  <div class="info-panel" role="group" aria-label="Öffnungszeiten und Kontakt auf zartem Damastgrund">
    <h2 class="info-title">Öffnungszeiten</h2>
    <dl class="hours">
      <dt>Montag - Samstag</dt><dd></dd>
      <dt>Mo, Di, Do &amp; Fr</dt><dd>09.30 - 13.00 Uhr</dd>
      <dt></dt><dd>14.30 - 18.00 Uhr</dd>
    </dl>
    <h2 class="info-title">Kontakt</h2>
    <address class="contact">
      Behrens Bastel und Dekorieren<br>
      Lindenweg 12<br>
      21000 Musterstadt
      <ul class="contact-lines">
        <li><svg viewBox="0 0 16 16"><path d="M3 2h3l1.5 3.5-2 1.2a8 8 0 0 0 3.8 3.8l1.2-2L14 10v3a1 1 0 0 1-1 1A11 11 0 0 1 2 3a1 1 0 0 1 1-1z"/></svg>01234 - 56 78 90</li>
        <li><svg viewBox="0 0 16 16"><path d="M3 2h3l1.5 3.5-2 1.2a8 8 0 0 0 3.8 3.8l1.2-2L14 10v3a1 1 0 0 1-1 1A11 11 0 0 1 2 3a1 1 0 0 1 1-1z"/></svg>01234 - 56 78 91</li>
        <li><svg viewBox="0 0 16 16"><path d="M1 3h14v10H1z M2 4l6 5 6-5" fill="none" stroke="#4b97a2" stroke-width="1.6"/></svg>info@falten-und-kleben.example</li>
      </ul>
    </address>
  </div>
  <div class="band band--bottom"></div>
  <p class="claim">Aus einfachen schöne und edle Dinge machen</p>
  <p class="slogan">Wir zeigen es Ihnen</p>
</section>

</body>
</html>
```